Nobre Lente Lusitana - business card

Create a business card for my eyewear (glasses) store. The concept is based in handcrafted glasses (as well as common frames and 3d printed), clean, and elegant. The business card could be black (white letters and symbols) or white (black letters and symbols) but we are open to new suggestions. It must be sober and elegant.
The name Nobre Lente Lusitana means Royal/Real Portuguese Optical Store.
Our concept should be inspired by the pictures attatched bellow.
I would like it to be classic and elegant as business cards for bankers.
Our first selected logo is also available in attachment files.

Target Market(s)

For business meetings with investors, supliers and fairs

Industry/Entity Type

Eyewear

Contact Information for Business Card

Some random business cards in attachment that we like. Don't be closed to it, we like freedom of think.

Font styles to use
Serif
Sans Serif

Colors
404040
e9e9e9
fbfbfb
000000
85abd3
0255a3
f7fbfd
959595

Requirements
Must have
• Must be elegant, simple.
• Must present our brand new logo (slight variations are welcome, the logo is not closed yet). See our temporary logo in attachment.
• Black (or dark grey), white (or light grey) and a third slight color.
• This third slight color could be dark blue or grayish blue.
• Info:
• Tomás Vidigal (name)
• tvidigal@nobrelentelusitana.example
• +351 927364051
• www.nobrelentelusitana.example
Nice to have
• Black and white or with serious colors such as dark blue or greyish blue.
• Could also have water mark with our logo (big size) in the background (inspired in KMT bank credit card design)
Should not have
• Hysteric colora or shapes

```html
<!DOCTYPE html>
<html lang="pt">
<head>
<meta charset="utf-8">
<title>Nobre Lente Lusitana – Business Card</title>
<link rel="stylesheet" href="https://fonts.googleapis.com/css2?family=Montserrat:wght@400;500;600;700&display=swap">
<style>
  :root {
    --backdrop: #e4e4e5;
    --card: #ffffff;
    --ink: #1a1a1a;
    --ink-soft: #404040;
    --rule: #595959;
    --shadow: rgba(0, 0, 0, 0.18);
  }
  * { box-sizing: border-box; margin: 0; padding: 0; }
  html, body {
    width: 1200px;
    height: 1200px;
    overflow: hidden;
    background: var(--backdrop);
    font-family: "Montserrat", sans-serif;
    color: var(--ink);
  }
  .canvas {
    position: relative;
    width: 1200px;
    height: 1200px;
  }
  .card {
    position: absolute;
    left: 250px;
    width: 700px;
    height: 400px;
    background: var(--card);
    box-shadow: 0 6px 16px var(--shadow);
  }
  .card--front { top: 170px; }
  .card--back  { top: 630px; }

  .brand {
    display: flex;
    align-items: center;
    gap: 12px;
    font-weight: 600;
    font-size: 22px;
    letter-spacing: 0.06em;
    text-transform: uppercase;
    color: var(--ink);
    white-space: nowrap;
  }
  .brand__dot {
    width: 14px;
    height: 14px;
    border: 2.5px solid var(--ink);
    border-radius: 50%;
    flex: none;
  }

  .card--front .brand {
    position: absolute;
    left: 50%;
    top: 50%;
    transform: translate(-50%, -50%);
  }

  .card--back .brand {
    position: absolute;
    right: 48px;
    top: 92px;
    font-size: 19px;
  }
  .card--back .top-rule {
    position: absolute;
    left: 300px;
    right: 40px;
    top: 150px;
    height: 1.5px;
    background: var(--rule);
  }

  .person {
    position: absolute;
    left: 44px;
    bottom: 148px;
  }
  .person__name {
    font-weight: 700;
    font-size: 26px;
    letter-spacing: -0.01em;
    text-transform: uppercase;
    line-height: 1.1;
  }
  .person__role {
    font-weight: 500;
    font-size: 17px;
    letter-spacing: 0.12em;
    text-transform: uppercase;
    margin-top: 4px;
    color: var(--ink-soft);
  }
  .mid-rule {
    position: absolute;
    left: 44px;
    width: 420px;
    bottom: 132px;
    height: 1.5px;
    background: var(--rule);
  }

  .contacts {
    position: absolute;
    left: 44px;
    bottom: 30px;
    list-style: none;
  }
  .contacts__item {
    display: flex;
    align-items: center;
    gap: 12px;
    font-size: 14px;
    font-weight: 500;
    letter-spacing: 0.1em;
    text-transform: uppercase;
    line-height: 28px;
  }
  .contacts__item:first-child { letter-spacing: 0.04em; font-size: 15px; }
  .contacts__icon { width: 12px; height: 12px; fill: var(--ink); flex: none; }
</style>
</head>
<body>
<main class="canvas">

  <section class="card card--front" aria-label="Card front">
    <div class="brand"><span class="brand__dot"></span>Nobre Lente Lusitana</div>
  </section>

  <section class="card card--back" aria-label="Card back">
    <div class="brand"><span class="brand__dot"></span>Nobre Lente Lusitana</div>
    <div class="top-rule"></div>

    <div class="person">
      <p class="person__name">Tomás Vidigal</p>
      <p class="person__role">President</p>
    </div>
    <div class="mid-rule"></div>

    <ul class="contacts">
      <li class="contacts__item">
        <svg class="contacts__icon" viewBox="0 0 12 12" aria-hidden="true"><path d="M3 0.5 L4.6 3.2 L3.4 4.4 C4 6 6 8 7.6 8.6 L8.8 7.4 L11.5 9 L10.5 11.2 C5.5 11.2 0.8 6.5 0.8 1.5 Z"/></svg>
        +351 927364051
      </li>
      <li class="contacts__item">
        <svg class="contacts__icon" viewBox="0 0 12 12" aria-hidden="true"><path d="M0.5 2 H11.5 V10 H0.5 Z M1.2 2.6 L6 6.4 L10.8 2.6" stroke="#fff" stroke-width="0.9"/></svg>
        tvidigal@nobrelentelusitana.example
      </li>
      <li class="contacts__item">
        <svg class="contacts__icon" viewBox="0 0 12 12" aria-hidden="true"><circle cx="6" cy="6" r="5.5"/><path d="M0.8 6 H11.2 M6 0.6 C3.5 3.5 3.5 8.5 6 11.4 M6 0.6 C8.5 3.5 8.5 8.5 6 11.4" stroke="#fff" stroke-width="0.8" fill="none"/></svg>
        www.nobrelentelusitana.example
      </li>
    </ul>
  </section>

</main>
</body>
</html>
```